Project VELI

I am setting up a consultancy company in Istanbul, Turkey called VELI Partners. VELI partners will focus areas are highlighted in the attached presenatation. Expertise area as follows; Corporate Communications, Digitilization and Technology Integration, CSR & Sponsorships, Investor Relations and Fİnancial PR, Strategic Transactions, Corporate Governance... In related arease Project Management and Training support given.. For details see presenations. Our company collars are marun and blue.. In the attached presenations you can also see the business card colars and logo design. The design should reflect innovationi technology knowhow and power of communications skills. Enclosed you can find a presentations of scope of consultancy services and corporate logo from which logo and colars can be adapted..

Target Market(s)

Potential clients are any Holding or Company that would need services defined in the presantation attached.

Industry/Entity Type

It Company

Coding

Coded - Design and coding required

Number of Pages Required

5+ page

Font styles to use
Sans Serif

Requirements
Must have
• Main Expertize areas are defined in the presentation. The clients should be able to clearly see these and as they select the related area go to related page to see the content detail. I should be to also include vision statement in front page.. I should be able to present partners of the company in a related section. site should allow posting of pictures and an introductory video... Please use the logo and colars ı provided on attached file. Marun should be the dominating colar.
Nice to have
• www.morvanthrel.com I like.. Morvant provides somewhat similar services world wide. You can check out the site but don't need to necessarly do the same..

```html
<!DOCTYPE html>
<html lang="en">
<head>
<meta charset="utf-8">
<title>VELI Partners</title>
<link href="https://fonts.googleapis.com/css2?family=Open+Sans:wght@400;600;700&display=swap" rel="stylesheet">
<style>
:root{
  --maroon:#6a0d50;
  --maroon-dark:#5a0a44;
  --blue:#27348b;
  --ink:#3a3a3a;
  --nav:#555;
  --card-bg:#f8f8f8;
  --footer:#333333;
  --footer-text:#ffffff;
  --footer-line:#5a5a5a;
  --btn-grey:#4a4a4a;
}
*{margin:0;padding:0;box-sizing:border-box}
html,body{width:1200px;height:2244px;overflow:hidden;background:#fff}
body{position:relative;font-family:"Open Sans",Arial,sans-serif;color:var(--ink)}
.abs{position:absolute}

/* header */
.brand{left:132px;top:44px;display:flex;align-items:center;gap:10px;font-size:38px;font-weight:700;color:var(--blue);letter-spacing:1px}
.brand-mark{width:22px;height:22px;background:var(--blue)}
.brand small{font-size:38px;font-weight:700}
.search{left:791px;top:16px;width:277px;height:32px;border:1px solid #aaa;font-size:12px;color:#666;padding:7px 10px}
.search svg{position:absolute;right:10px;top:8px}
.nav{top:76px;right:132px;display:flex;gap:0;font-size:14.5px;color:var(--nav)}
.nav a{color:inherit;text-decoration:none;margin-left:54px}
.nav a.active{color:var(--maroon)}

/* hero */
.hero{left:0;top:124px;width:1200px;height:561px;background:linear-gradient(100deg,#c8d3df 0%,#e9edf2 35%,#f4f6f8 55%,#cfd6de 80%,#8e9aa8 100%)}
.hero-panel{left:699px;top:347px;width:369px;height:274px;background:rgba(40,40,40,.82);color:#fff;padding:22px 35px}
.hero-panel h1{font-size:45px;font-weight:600;line-height:1.15;margin-bottom:14px}
.hero-panel p{font-size:21px;line-height:30px}
.dots{display:flex;gap:5px;margin-top:22px}
.dots span{width:10px;height:10px;border-radius:50%;background:#fff}
.dots span.on{background:var(--maroon)}

/* sections */
.heading{left:0;width:1200px;text-align:center;color:var(--maroon);font-size:30px;font-weight:700}
.lead{left:150px;width:900px;text-align:center;font-size:14.5px;line-height:24px}
.video{left:132px;top:928px;width:426px;height:236px;background:linear-gradient(180deg,#eef1f4 0%,#d9dee4 60%,#a9b0b8 100%)}
.video-bar{position:absolute;left:0;bottom:0;width:100%;height:26px;background:#1d1d1d}
.video-bar i{position:absolute;left:14px;top:8px;width:0;height:0;border-left:9px solid #ccc;border-top:5px solid transparent;border-bottom:5px solid transparent}
.video-bar b{position:absolute;left:36px;right:14px;top:12px;height:2px;background:#555}
.intro-text{left:598px;top:924px;width:460px;font-size:14.5px;line-height:24.4px}
.btn{display:flex;align-items:center;justify-content:center;background:var(--maroon);color:#fff;font-size:17px;font-weight:600;text-decoration:none}

.card{top:1337px;width:281px;height:358px;background:var(--card-bg);border-bottom:3px solid var(--maroon)}
.card-photo{width:281px;height:176px}
.card h3{font-size:18px;font-weight:700;color:var(--maroon);margin:20px 22px 10px}
.card p{font-size:13.5px;line-height:24px;margin:0 22px}
.card a{display:block;margin:12px 22px 0;font-size:13.5px;color:var(--maroon);text-decoration:none}

/* footer */
.footer{left:0;top:1858px;width:1200px;height:386px;background:var(--footer);color:var(--footer-text)}
.fcol{top:48px}
.fcol h4{font-size:17px;font-weight:600;margin-bottom:12px}
.fcol p,.fcol li{font-size:13px;line-height:24.4px;list-style:none}
.email{width:313px;height:37px;background:#fff;color:#444;font-size:13px;padding:9px 13px;margin-top:20px}
.subscribe{width:134px;height:37px;background:var(--btn-grey);color:#fff;font-size:17px;font-weight:600;display:flex;align-items:center;justify-content:center;margin-top:20px}
.rule{left:132px;top:287px;width:936px;height:1px;background:var(--footer-line)}
.copy{left:132px;top:325px;font-size:13px}
.social{top:318px;left:937px;display:flex;gap:18px}
.social span{width:32px;height:32px;border-radius:50%;background:#4a4a4a}
</style>
</head>
<body>

<header>
  <div class="abs brand"><span class="brand-mark"></span>VELI <small>partners</small></div>
  <div class="abs search">Search here...
    <svg width="16" height="16" viewBox="0 0 16 16"><circle cx="6.5" cy="6.5" r="4.8" fill="none" stroke="#6a0d50" stroke-width="2"/><line x1="10" y1="10" x2="14.5" y2="14.5" stroke="#6a0d50" stroke-width="2.4"/></svg>
  </div>
  <nav class="abs nav">
    <a class="active" href="#">Home</a><a href="#">About Us</a><a href="#">What We Do</a><a href="#">Latest Blog</a><a href="#">Contact Us</a>
  </nav>
</header>

<section class="abs hero" role="img" aria-label="Photo of business partners smiling in a meeting around a table"></section>
<div class="abs hero-panel">
  <h1>Veli Partners</h1>
  <p>Lorem ipsum dolor sit amet, eam malis etiam deterruisset ea, inani albucius reprehendunt sea cu. Nam viris qualisque.</p>
  <div class="dots"><span class="on"></span><span></span><span></span><span></span></div>
</div>

<h2 class="abs heading" style="top:716px">Our Vision</h2>
<p class="abs lead" style="top:766px">Lorem ipsum dolor sit amet, eam malis etiam deterruisset ea, inani albucius reprehendunt sea cu. Nam viris qualisque consetetur ad. Eam integre oporteat ut, ne ullum percipit recusabo sed. Ne omnium discere persequeris sit, quo suas contentiones in.Cum liber saperet at, ne audiam nostrud volumus vel, nam aliquam singulis posidonium ea. Te vim veri verear.</p>

<h2 class="abs heading" style="top:863px">Introductory Video</h2>
<div class="abs video" role="img" aria-label="Introductory video still of a team meeting in a bright office">
  <div class="video-bar"><i></i><b></b></div>
</div>
<p class="abs intro-text">Cum liber saperet at, ne audiam nostrud volumus vel, nam aliquam singulis posidonium ea. Te vim veri verear. Nostrud bonorum consectetuer id sed, sumo inani his cu, posse dicunt interpretaris in cum. An consequat tincidunt eos, his cu dictas option nusquam, est an viris interpretaris. Dicat nemore iuvaret eos ne, agam malorum eos an. Detraxit scribentur disputationi qui in.Dicat nemore iuvaret eos ne, agam malorum eos an. Detraxit scribentur disputationi qui in.</p>
<a class="abs btn" href="#" style="left:600px;top:1115px;width:144px;height:50px">Read more</a>

<h2 class="abs heading" style="top:1211px">What We Do</h2>
<p class="abs lead" style="top:1266px">Lorem ipsum dolor sit amet, eam malis etiam deterruisset ea, inani albucius reprehendunt sea cu. Nam viris qualisque consetetur ad. Eam integre oporteat ut, ne ullum percipit recusabo sed. Ne omnium discere persequeris sit, quo suas contentiones in.</p>

<article class="abs card" style="left:132px">
  <div class="card-photo" role="img" aria-label="Photo of colleagues talking at a business event" style="background:linear-gradient(160deg,#dfe6ee,#b7c3d1)"></div>
  <h3>Corporate Communications</h3>
  <p>Lorem ipsum dolor sit amet, eam malis etiam deterruisset ea, inani albucius reprehendunt sea cu isque.</p>
  <a href="#">Read more</a>
</article>
<article class="abs card" style="left:459px">
  <div class="card-photo" role="img" aria-label="Photo of hands using a calculator over financial papers" style="background:linear-gradient(160deg,#9a9ea3,#e4e6e8)"></div>
  <h3>Strategic Transactions</h3>
  <p>Lorem ipsum dolor sit amet, eam malis etiam deterruisset ea, inani albucius reprehendunt sea cu isque.</p>
  <a href="#">Read more</a>
</article>
<article class="abs card" style="left:787px">
  <div class="card-photo" role="img" aria-label="Photo of a support agent wearing a headset" style="background:linear-gradient(160deg,#c9d3dc,#e8d8c0)"></div>
  <h3>CSR &amp; Sponsorships</h3>
  <p>Lorem ipsum dolor sit amet, eam malis etiam deterruisset ea, inani albucius reprehendunt sea cu isque.</p>
  <a href="#">Read more</a>
</article>

<a class="abs btn" href="#" style="left:491px;top:1741px;width:220px;height:51px">View all services</a>

<footer class="abs footer">
  <div class="abs fcol" style="left:132px;width:260px">
    <h4>About Us</h4>
    <p>Cum liber saperet at, ne audiam nostrud volumus vel, nam aliquam singulis posidonium ea. Te vim veri verear. Nostrud bonorum consectetuer id sed, sumo inani his cu, posse dicunt interpretaris in cum. An consequat tincidunt eos, his cu dictas option nusquam, est an viris.</p>
  </div>
  <div class="abs fcol" style="left:455px;width:280px">
    <h4>What We Do</h4>
    <ul>
      <li>Corporate Communications</li>
      <li>Digitilization and Technology Integration</li>
      <li>CSR &amp; Sponsorships</li>
      <li>Investor Relations and Fİnancial PR</li>
      <li>Strategic Transactions</li>
      <li>Corporate Governance</li>
    </ul>
  </div>
  <div class="abs fcol" style="left:755px;width:313px">
    <h4>Newsletter Signup</h4>
    <p>Lorem ipsum dolor sit amet, eam malis etiam deterruisset ea, inani albucius reprehendunt seacu.</p>
    <div class="email">Enter your email</div>
    <div class="subscribe">Subscribe</div>
  </div>
  <div class="abs rule"></div>
  <p class="abs copy">Copyright @ 2014 Veli Partners.All Rights Reserved.</p>
  <div class="abs social"><span></span><span></span><span></span></div>
</footer>

</body>
</html>
```